Kestro Vale - Dog Supplement Brand

Here a link to a word doc with all of my info.
Please read it carefully.
https://files.brindlepad.net/sheet/7QwLx2mTa8Rk3PzNv0eYc5Hj9UfGs46Bd1Oi-Lp-3/view?ref=shared
Its 2 pages. Home Page and Product Page.
Oh and btw: the poses I attached dont have a shadow, so it would be good if you added a shadow to the poses .
If you have any questions please let me know.
Target Market(s)
Dog Owners In UK
Industry/Entity Type
Dog supplements
Number of Pages Required
2 page
Requirements
Must have
- Home page and product page files. Super Hero Theme.

```html
<!DOCTYPE html>
<html lang="en">
<head>
<meta charset="utf-8">
<title>Kestro Vale – Home</title>
<link href="https://fonts.googleapis.com/css2?family=Kanit:ital,wght@0,700;0,800;1,700;1,800;1,900&family=Poppins:wght@400;500;600;700&display=swap" rel="stylesheet">
<style>
:root{
  --red:#e3101f;
  --red-dark:#b80c18;
  --blue:#2fa6ea;
  --blue-light:#9fd8f8;
  --yellow:#f8b400;
  --orange:#f39a12;
  --ink:#111111;
  --muted:#555555;
  --white:#ffffff;
  --paper:#f4f4f4;
  --line:#dddddd;
}
*{box-sizing:border-box;margin:0;padding:0}
html,body{width:1200px;height:3832px;overflow:hidden}
body{font-family:"Poppins",sans-serif;color:var(--ink);background:var(--white);position:relative}
.display{font-family:"Kanit",sans-serif;font-style:italic;font-weight:800}

/* announcement */
.topbar{height:28px;background:var(--red);color:var(--white);font-size:11px;font-weight:500;display:flex;align-items:center;justify-content:center;letter-spacing:.2px}

/* header */
.site-header{height:92px;display:flex;align-items:center;justify-content:space-between;padding:0 64px;background:var(--white)}
.site-header .icon{width:22px;height:22px}
.brand{display:flex;align-items:center;gap:10px;font-family:"Kanit",sans-serif;font-weight:800;font-size:30px;color:var(--ink);text-transform:uppercase;letter-spacing:.5px}
.brand .dot{width:18px;height:18px;border-radius:50%;background:var(--red)}
.header-tools{display:flex;gap:22px}

/* hero */
.hero{position:relative;height:620px;background:radial-gradient(circle at 25% 55%,var(--blue-light) 0%,var(--blue) 55%,#1e8fd6 100%);overflow:hidden}
.hero-art{position:absolute;left:150px;top:40px;width:520px;height:570px;border-radius:46% 54% 40% 60%;background:radial-gradient(circle at 50% 45%,#eef4f8 0%,#b9c8d4 45%,rgba(227,16,31,.55) 80%,rgba(227,16,31,0) 100%)}
.hero-copy{position:absolute;left:680px;top:200px;width:460px}
.hero-copy h1{font-size:48px;line-height:1.02;color:var(--white);text-shadow:3px 3px 0 rgba(0,0,0,.25)}
.btn{display:inline-flex;align-items:center;justify-content:center;border-radius:40px;font-family:"Poppins",sans-serif;font-weight:700;font-size:13px;text-transform:uppercase;letter-spacing:.3px}
.btn-red{background:var(--red);color:var(--white)}
.btn-white{background:var(--white);color:var(--red)}
.hero .btn{margin-top:38px;width:160px;height:54px;font-size:15px;font-style:italic;font-family:"Kanit",sans-serif;box-shadow:0 4px 0 var(--red-dark)}

/* products */
.products{position:relative;height:940px;background:var(--paper);padding-top:58px}
.section-title{text-align:center;font-size:40px;color:var(--ink)}
.product-row{display:flex;justify-content:center;gap:52px;margin-top:46px}
.product-row + .product-row{margin-top:34px}
.product{width:214px;text-align:center}
.product-art{height:206px;border-radius:10px}
.product h3{font-family:"Kanit",sans-serif;font-style:italic;font-weight:800;font-size:22px;line-height:1.1;margin-top:12px}
.product p{font-size:13px;color:var(--muted);line-height:1.45;margin-top:8px}
.product .btn{width:106px;height:36px;margin-top:14px}
.art-gold{background:radial-gradient(circle,#fff1a6 0%,#f6c21a 60%,#e8a800 100%)}
.art-red{background:radial-gradient(circle,#ffd6d6 0%,#e84552 60%,#c1121f 100%)}
.art-purple{background:radial-gradient(circle,#e8d6ff 0%,#8a4fe0 60%,#5b2aa8 100%)}
.art-teal{background:radial-gradient(circle,#d6fff6 0%,#36c7b0 60%,#1d8f7e 100%)}
.art-orange{background:radial-gradient(circle,#ffe7c4 0%,#f59c2a 60%,#d9700e 100%)}

/* about */
.about{position:relative;height:640px;background:var(--white)}
.about-band{position:absolute;left:0;right:0;top:120px;height:440px;background:linear-gradient(90deg,var(--red) 0%,var(--red) 60%,#ef4050 100%)}
.about-copy{position:absolute;left:110px;top:170px;width:590px;color:var(--white)}
.about-copy h2{font-size:34px;text-transform:uppercase}
.about-copy p{font-size:13px;line-height:1.6;margin-top:14px}
.about-copy .btn{width:210px;height:48px;margin-top:34px}
.about-art{position:absolute;left:770px;top:40px;width:400px;height:580px;border-radius:48% 52% 40% 40%;background:linear-gradient(180deg,#f1f3f5 0%,#bcc6cf 55%,#d23040 100%)}

/* testimonials */
.reviews{height:500px;text-align:center;padding-top:100px}
.reviews h2{font-size:38px;text-transform:uppercase}
.avatars{display:flex;justify-content:center;margin-top:30px}
.avatar{width:62px;height:62px;border-radius:50%;border:3px solid var(--white);margin:0 -6px}
.avatar.a1{background:#c9a58c}.avatar.a2{background:#8f6b5c;width:74px;height:74px;margin-top:-6px;z-index:1}.avatar.a3{background:#b0b8c2}
.reviews h4{font-family:"Kanit",sans-serif;font-style:italic;font-size:22px;margin-top:8px}
.reviews .date{font-size:12px;color:var(--muted)}
.reviews blockquote{width:700px;margin:26px auto 0;font-size:13px;line-height:1.6;color:#333}
.dots{display:flex;justify-content:center;gap:8px;margin-top:30px}
.dots span{width:9px;height:9px;border-radius:50%;background:#f2a3aa}
.dots span.on{background:var(--red)}

/* certification */
.certified{position:relative;height:460px;background:linear-gradient(90deg,var(--yellow) 0%,var(--orange) 100%);overflow:hidden}
.cert-art{position:absolute;left:80px;top:30px;width:480px;height:400px;border-radius:44% 56% 50% 50%;background:radial-gradient(circle,#ffffff 0%,#d9e6f0 40%,rgba(47,166,234,.6) 75%,rgba(47,166,234,0) 100%)}
.cert-copy{position:absolute;left:600px;top:50px;width:500px;color:var(--white)}
.cert-copy h2{font-size:40px;text-transform:uppercase}
.cert-copy p{font-size:13px;line-height:1.6;margin-top:12px}
.badges{display:flex;gap:34px;margin-top:40px}
.badge{width:76px;height:76px;border-radius:50%;border:3px solid rgba(255,255,255,.9);background:rgba(255,255,255,.15)}

/* why */
.why{height:380px;background:var(--paper);padding-top:64px;text-align:center}
.why h2{font-size:40px;text-transform:uppercase}
.why-cards{display:flex;justify-content:center;gap:32px;margin-top:36px}
.why-card{width:292px;height:208px;background:var(--white);border-radius:10px;box-shadow:0 6px 22px rgba(0,0,0,.12);display:flex;flex-direction:column;align-items:center;padding-top:28px}
.why-icon{width:68px;height:68px;border-radius:50%;background:var(--orange);display:flex;align-items:center;justify-content:center}
.why-card h3{font-family:"Kanit",sans-serif;font-style:italic;font-weight:800;font-size:20px;line-height:1.15;margin-top:18px;width:230px}

/* footer */
.site-footer{height:172px;border-top:1px solid var(--line);padding:38px 64px 0;display:flex;justify-content:space-between}
.region label{display:block;font-size:11px;color:var(--muted)}
.region .select{margin-top:8px;width:190px;height:38px;border:1px solid #999;font-size:12px;display:flex;align-items:center;justify-content:space-between;padding:0 12px}
.pay{text-align:right}
.pay-icons{display:flex;gap:6px}
.pay-icons span{width:38px;height:24px;border-radius:4px;border:1px solid var(--line);background:#eef0f2}
.pay small{display:block;font-size:10px;color:var(--muted);margin-top:12px}
</style>
</head>
<body>

<div class="topbar">FREE Shipping on all orders over £30 &gt;&gt; Get your first bottle 15% off when you join the squad!</div>

<header class="site-header">
  <svg class="icon" viewBox="0 0 24 24"><path d="M3 6h18M3 12h18M3 18h18" stroke="#111" stroke-width="2"/></svg>
  <div class="brand"><span class="dot"></span>Kestro Vale</div>
  <div class="header-tools">
    <svg class="icon" viewBox="0 0 24 24" fill="none" stroke="#111" stroke-width="2"><circle cx="10" cy="10" r="6"/><path d="M15 15l6 6"/></svg>
    <svg class="icon" viewBox="0 0 24 24" fill="none" stroke="#111" stroke-width="2"><circle cx="12" cy="8" r="4"/><path d="M4 21c1-5 15-5 16 0"/></svg>
    <svg class="icon" viewBox="0 0 24 24" fill="none" stroke="#111" stroke-width="2"><path d="M5 8h14l-1 13H6z"/><path d="M9 8a3 3 0 016 0"/></svg>
  </div>
</header>

<section class="hero">
  <div class="hero-art" role="img" aria-label="Superhero husky mascot flexing in a red cape over a comic burst"></div>
  <div class="hero-copy">
    <h1 class="display">Join Forces With Kestro Vale &amp; Let Him Be Your Beloved Dog's Hero!</h1>
    <span class="btn btn-red">Join Forces!</span>
  </div>
</section>

<section class="products">
  <h2 class="section-title display">Our Products</h2>
  <div class="product-row">
    <div class="product"><div class="product-art art-gold" role="img" aria-label="Multivitamin supplement pouch"></div><h3>Super Multivits</h3><p>Lorem ipsum dolor sit amet, consectetur adipiscing</p><span class="btn btn-red">Shop Now</span></div>
    <div class="product"><div class="product-art art-red" role="img" aria-label="Omega 3,6,9 supplement pouch"></div><h3>Super Omega 3,6,9</h3><p>Lorem ipsum dolor sit amet, consectetur adipiscing</p><span class="btn btn-red">Shop Now</span></div>
    <div class="product"><div class="product-art art-purple" role="img" aria-label="Probiotics supplement pouch"></div><h3>Super Probiotics</h3><p>Lorem ipsum dolor sit amet, consectetur adipiscing</p><span class="btn btn-red">Shop Now</span></div>
    <div class="product"><div class="product-art art-teal" role="img" aria-label="Calming supplement pouch"></div><h3>Calm Kestro</h3><p>Lorem ipsum dolor sit amet, consectetur adipiscing</p><span class="btn btn-red">Shop Now</span></div>
  </div>
  <div class="product-row">
    <div class="product"><div class="product-art art-orange" role="img" aria-label="Joint support supplement pouch"></div><h3>Super Joint Support</h3><p>Lorem ipsum dolor sit amet, consectetur adipiscing</p><span class="btn btn-red">Shop Now</span></div>
    <div class="product"><div class="product-art art-red" role="img" aria-label="Digestive support supplement pouch"></div><h3>Super Digestive Support</h3><p>Lorem ipsum dolor sit amet, consectetur adipiscing</p><span class="btn btn-red">Shop Now</span></div>
    <div class="product"><div class="product-art art-orange" role="img" aria-label="Urinary support supplement pouch"></div><h3>Super Urinary Support</h3><p>Lorem ipsum dolor sit amet, consectetur adipiscing</p><span class="btn btn-red">Shop Now</span></div>
  </div>
</section>

<section class="about">
  <div class="about-band"></div>
  <div class="about-copy">
    <h2 class="display">Hi! I'm Kestro Vale!</h2>
    <p>Lorem ipsum dolor sit amet, consectetur adipiscing elit, sed do eiusmod tempor incididunt ut labore et dolore magna aliqua. Quis ipsum suspendisse ultrices gravida. Risus commodo viverra maecenas accumsan lacus vel facilisis. Lorem ipsum dolor sit amet, consectetur adipiscing elit, sed do eiusmod tempor incididunt ut labore et dolore magna aliqua. Quis ipsum suspendisse ultrices gravida. Risus commodo viverra maecenas accumsan lacus vel facilisis. Lorem ipsum dolor sit amet, consectetur adipiscing elit, sed do eiusmod.</p>
    <span class="btn btn-white">Read More About Me</span>
  </div>
  <div class="about-art" role="img" aria-label="Superhero husky mascot standing and waving, with a soft ground shadow"></div>
</section>

<section class="reviews">
  <h2 class="display">People Love Me</h2>
  <div class="avatars">
    <span class="avatar a1" role="img" aria-label="Customer portrait"></span>
    <span class="avatar a2" role="img" aria-label="Customer portrait"></span>
    <span class="avatar a3" role="img" aria-label="Customer portrait"></span>
  </div>
  <h4>Mara Linwood</h4>
  <div class="date">January 23, 2023</div>
  <blockquote>Lorem ipsum dolor sit amet, consectetur adipiscing elit, sed do eiusmod tempor incididunt ut labore et dolore magna aliqua. Quis ipsum suspendisse ultrices gravida. Risus commodo viverra maecenas accumsan lacus vel facilisis. Use this text to share information about your brand with your customers.</blockquote>
  <div class="dots"><span></span><span class="on"></span><span></span><span></span></div>
</section>

<section class="certified">
  <div class="cert-art" role="img" aria-label="Superhero husky mascot holding a certificate inside a comic burst"></div>
  <div class="cert-copy">
    <h2 class="display">Regulated &amp; Certified</h2>
    <p>Lorem ipsum dolor sit amet, consectetur adipiscing elit, sed do eiusmod tempor incididunt ut labore et dolore magna aliqua. Quis ipsum suspendisse ultrices gravida. Risus commodo viverra maecenas accumsan lacus vel facilisis. Lorem ipsum dolor sit amet, consectetur adipiscing elit, sed do eiusmod tempor incididunt ut labore et dolore magna aliqua. Quis ipsum suspendisse ultrices gravida. Risus commodo viverra maecenas accumsan lacus vel facilisis.</p>
    <div class="badges"><span class="badge"></span><span class="badge"></span><span class="badge"></span></div>
  </div>
</section>

<section class="why">
  <h2 class="display">Why Choose Me?</h2>
  <div class="why-cards">
    <div class="why-card">
      <div class="why-icon"><svg width="34" height="34" viewBox="0 0 24 24" fill="none" stroke="#fff" stroke-width="2"><path d="M5 19C5 9 11 5 20 4c-1 9-5 15-15 15z"/><path d="M5 19l8-8"/></svg></div>
      <h3>Only Organic &amp; Natural Ingredients</h3>
    </div>
    <div class="why-card">
      <div class="why-icon"><svg width="34" height="34" viewBox="0 0 24 24" fill="none" stroke="#fff" stroke-width="2"><path d="M3 12V4h8l10 10-8 8z"/><circle cx="7.5" cy="7.5" r="1.5"/></svg></div>
      <h3>20% OFF For All Kestro Vale Squad Members</h3>
    </div>
    <div class="why-card">
      <div class="why-icon"><svg width="34" height="34" viewBox="0 0 24 24" fill="none" stroke="#fff" stroke-width="2"><path d="M2 6h12v10H2zM14 10h4l3 3v3h-7"/><circle cx="6" cy="18" r="2"/><circle cx="17" cy="18" r="2"/></svg></div>
      <h3>Free Next Day UK Delivery</h3>
    </div>
  </div>
</section>

<footer class="site-footer">
  <div class="region">
    <label>Country/region</label>
    <div class="select">United Kingdom (GBP £) <svg width="10" height="6" viewBox="0 0 10 6"><path d="M1 1l4 4 4-4" stroke="#111" fill="none"/></svg></div>
  </div>
  <div class="pay">
    <div class="pay-icons"><span></span><span></span><span></span><span></span><span></span><span></span><span></span><span></span><span></span></div>
    <small>© 2023, Kestro Vale</small>
  </div>
</footer>

</body>
</html>
```